Social Fitness Contest Site

Updated 6/30/2013: Leaning for a Red, black, white and either tan or grey color scheme.
The concept is a social fitness contest website. We will have daily, weekly, and monthly "physical challenges" that will be posted by our admins that will allow anyone to submit scores for the opportunity to win prizes.
Example: Weekly Contest: Complete as many push ups as possible in 5 minutes.
People will come to the site, review the open contests, and submit a score if they like. The first version of the site will operate on a single page using only in-line popups for registration and score submission.
Design guidelines:
- large fonts for items like workout title, end time, score submit button, and prizes can be large.
- normal size fonts for elements like athlete and gym rankings as well as leaderboard
HOMEPAGE:
- logo top left hand corner
- Top right hand corner: FAQ - Contact Us - Submit Score
- FAQ will be in line popup of question and answers
- Contact us will be an in-line popup form submission
- see below for submit score option
- Workout Summary Section
- list current active workouts (about 5)
- recordset paging at bottom of page to access older workouts
Workout Details Block:
- workout name
- expandable workout description section
- icon to link to video which shows workout example
- submit score button
- status: Open, Ended, Upcoming
- top 10 leaders
- Athlete Name (Link to bio (venlotra page for now))
- Gym Name (Link to gym/affiliate (venlotra page for now))
- Measure (short text, example: "125" or "5:30")
- Link to video submission
- prizes
- 1st, 2nd, 3rd, other
- name of prize
- estimated value of prize ("A $200 Value")
- show prize thumbnail (1st place prize image larger)
- contest end time
Submit score:
- inline popup
- register w venlotra
- capture email on vl reg
- get mailing address for prizes (need address form design)
- sign in w venlotra
- score submission
- drop down of workouts (only show active workouts)
- pre-select workout clicked on
- allow multiple submissions for single workout. Use highest score submitted.
- Text Field for scoring method and label (reps, weight, time, etc)
- link to video URL on venlotra
- submit and cancel buttons
- backend validate vl video share url
- Athlete overall ranking on top right hand corner
- Ranking 1, 2, 3, etc
- Athlete name
- show total points
- show contest entered
- Team/affiliate ranking below it
- Similar to athlete ranking box)
"View All" for rankings
- athlete ranking
- workout ranking
- gym ranking
- in line popup
- name and stat fields
- recordset paging on bottom
- text search field on top right hand side of popup
- Right hand column for advertising partners
Note: We currently do not have a name or logo as of yet. We are open to color scheme suggestions.
Helmrand Athletes
Advertising

```html
<!DOCTYPE html>
<html lang="en">
<head>
<meta charset="utf-8">
<title>PeakTrial – Physical Challenges</title>
<link rel="stylesheet" href="https://fonts.googleapis.com/css2?family=Dosis:wght@300;400;500;600&display=swap">
<style>
:root{
  --blue:#2f8fb1;
  --red:#e23b3b;
  --green:#20a63a;
  --text:#4a4a4a;
  --page:#f1f1f1;
  --white:#ffffff;
  --line:#e4e4e4;
  --photo-a:#9a8a7e;
  --photo-b:#5b4f48;
  --video:#6e6e6e;
}
*{box-sizing:border-box;margin:0;padding:0}
html,body{width:708px;height:1200px;overflow:hidden}
body{font-family:"Dosis",sans-serif;color:var(--text);background:var(--page);position:relative}
h1,h2,h3,h4{font-weight:400}
a{color:inherit;text-decoration:none}

.site-header{position:absolute;left:0;top:0;width:708px;height:42px;background:var(--white);border-bottom:1px solid var(--line)}
.brand{position:absolute;left:116px;top:9px;font-size:20px;font-weight:500;color:var(--red);letter-spacing:-.5px}
.main-nav{position:absolute;right:122px;top:16px;display:flex;font-size:11px;color:#555}
.main-nav a{padding:0 10px;border-left:1px solid #ccc;line-height:11px;white-space:nowrap}
.main-nav a:first-child{border-left:0}
.main-nav a:last-child{padding-right:0}

.hero{position:absolute;left:0;top:42px;width:708px;height:158px;background:#f3f3f3;border-bottom:2px solid var(--blue);overflow:hidden;text-align:center}
.hero-arcs{position:absolute;left:0;top:0}
.hero-kicker{position:relative;margin-top:28px;font-size:20px;color:#555;letter-spacing:-.6px}
.hero-title{position:relative;font-size:46px;letter-spacing:-1.6px;line-height:44px;margin-top:2px}
.hero-title .blue{color:var(--blue)}
.hero-title .red{color:var(--red)}
.hero-actions{position:absolute;left:271px;top:115px;display:flex;gap:7px}
.btn{display:inline-block;color:var(--white);font-weight:500;border-radius:2px;white-space:nowrap;text-align:center}
.btn-red{background:var(--red)}
.btn-green{background:var(--green)}
.hero-actions .btn{width:79px;height:23px;line-height:23px;font-size:12.5px;letter-spacing:-.4px}

.weekly{position:absolute;left:0;top:202px;width:708px;height:170px;background:var(--white);border-bottom:1px solid var(--line)}
.weekly-label{position:absolute;left:116px;top:17px;font-size:16px;color:#444;letter-spacing:-.5px}
.weekly-title{position:absolute;left:116px;top:32px;font-size:24px;color:var(--red);letter-spacing:-.8px;white-space:nowrap}
.weekly-text{position:absolute;left:117px;top:68px;width:228px;font-size:6.3px;line-height:7.9px;color:#555}
.weekly-cta{position:absolute;left:117px;top:124px;width:143px;height:22px;line-height:22px;font-size:13px;letter-spacing:-.5px}
.scores{position:absolute;left:357px;top:66px;width:229px;height:86px;background:var(--blue);border-radius:2px;color:var(--white);padding:4px 7px}
.scores h3{font-size:14px;letter-spacing:-.4px;line-height:16px}
.scores table{width:100%;border-collapse:collapse;margin-top:4px;font-size:7.2px;line-height:9.2px}
.scores th{font-weight:600;text-align:center;white-space:nowrap}
.scores th:first-child,.scores td:first-child{text-align:left}
.scores td{text-align:center}

.section-title{position:absolute;font-size:15px;color:#555;letter-spacing:-.5px}

.contest{position:absolute;left:116px;width:378px;height:223px;background:var(--white);border:1px solid #e6e6e6;border-radius:2px}
.contest-title{position:absolute;left:6px;top:8px;font-size:12px;color:var(--blue);letter-spacing:-.4px;white-space:nowrap}
.contest-title small{font-size:8px;color:#555;margin-left:3px}
.status{position:absolute;right:6px;top:7px;display:flex;align-items:center;font-size:9px;color:#555;letter-spacing:-.2px}
.status .tag{background:var(--green);color:var(--white);font-size:7px;padding:1px 4px;border-radius:2px;margin-right:5px}
.contest-desc{position:absolute;left:6px;top:29px;width:291px;font-size:6.2px;line-height:7.9px;color:#555}
.contest-submit{position:absolute;left:6px;top:64px;width:62px;height:14px;line-height:14px;font-size:7px;letter-spacing:-.3px}
.video-thumb{position:absolute;left:308px;top:29px;width:63px;height:47px;background:var(--video);border-radius:1px}
.divider{position:absolute;left:6px;right:6px;height:1px;background:#ececec}
.leaders-title{position:absolute;left:6px;top:97px;font-size:12px;color:var(--blue);letter-spacing:-.4px}
.photo{position:absolute;background:linear-gradient(160deg,var(--photo-a),var(--photo-b))}
.photo-lead{left:6px;top:113px;width:57px;height:57px}
.lead-name{position:absolute;left:70px;top:114px;font-size:11px;color:var(--blue);letter-spacing:-.3px}
.lead-gym{position:absolute;left:70px;top:127px;font-size:8.5px;color:#555;white-space:nowrap}
.lead-video{position:absolute;left:70px;top:141px;font-size:7.5px;color:var(--blue);display:flex;align-items:center;white-space:nowrap}
.lead-video small{color:#aaa;margin-left:4px;font-size:6.5px}
.lead-prize{position:absolute;left:70px;top:156px;font-size:8px;color:#555}
.play-icon{width:9px;height:9px;margin-right:4px}
.runner{position:absolute;left:189px;width:130px}
.photo-runner{left:0;top:0;width:27px;height:27px}
.runner-name{position:absolute;left:31px;top:0;font-size:8px;color:var(--blue);letter-spacing:-.2px;white-space:nowrap}
.runner-gym{position:absolute;left:31px;top:10px;font-size:6px;color:#555;white-space:nowrap}
.runner-prize{position:absolute;left:31px;top:19px;font-size:6px;color:#555}
.runner-video{position:absolute;left:98px;top:0;font-size:4.8px;color:var(--blue);display:flex;align-items:center;white-space:nowrap}
.runner-video .play-icon{width:6px;height:6px;margin-right:2px}
.runner-time{position:absolute;left:106px;top:8px;font-size:4.8px;color:#bbb}
.others-label{position:absolute;left:6px;top:182px;font-size:7.5px;color:var(--blue)}
.others{position:absolute;left:6px;top:193px;display:flex;gap:4px}
.others .photo{position:static;width:27px;height:27px}

.partners{position:absolute;left:500px;top:400px;width:90px}
.partner{background:#dcdcdc;margin:0 auto}
.partner-1{width:60px;height:60px;border-radius:50%;margin-top:22px}
.partner-2{width:30px;height:70px;border-radius:15px;margin-top:22px}
.partner-3{width:84px;height:60px;margin-top:18px}
.partner-4{width:74px;height:74px;border-radius:50%;margin-top:16px}
.partner-5{width:74px;height:28px;margin-top:24px}
.partner-6{width:56px;height:20px;margin-top:8px;border-radius:10px}

.pager{position:absolute;left:118px;top:1117px;display:flex;align-items:center;gap:10px;font-size:9px;color:#555}
.pager .current{border-bottom:2px solid var(--blue);padding:0 3px}
.pager svg{display:block}

.site-footer{position:absolute;left:40px;top:1151px;width:628px;height:49px;border-top:1px solid #e3e3e3}
.footer-brand{position:absolute;left:76px;top:9px;font-size:20px;color:#aaa;letter-spacing:-.6px}
.copyright{position:absolute;right:82px;top:20px;font-size:5.5px;color:#555}
</style>
</head>
<body>

<header class="site-header">
  <a class="brand" href="#">PeakTrial</a>
  <nav class="main-nav">
    <a href="#">FAQs</a>
    <a href="#">Contact Us</a>
    <a href="#">Submit Score</a>
  </nav>
</header>

<section class="hero">
  <svg class="hero-arcs" width="708" height="158" viewBox="0 0 708 158" aria-hidden="true">
    <circle cx="330" cy="30" r="150" fill="none" stroke="#ebebeb" stroke-width="4"/>
    <circle cx="420" cy="60" r="120" fill="none" stroke="#eeeeee" stroke-width="3"/>
  </svg>
  <p class="hero-kicker">daily, weekly &amp; monthly</p>
  <h1 class="hero-title"><span class="blue">physical</span> <span class="red">challenges</span></h1>
  <div class="hero-actions">
    <a class="btn btn-red" href="#">Latest Contests</a>
    <a class="btn btn-green" href="#">Submit Score</a>
  </div>
</section>

<section class="weekly">
  <p class="weekly-label">This week's Contest</p>
  <h2 class="weekly-title">Complete as many push ups as possible in 5 minutes</h2>
  <p class="weekly-text">Set a timer for five minutes and do as many full push ups as you can. Keep your back straight and your chest low on each rep, with arms locked at the top. Film the full set from the side so every rep is clear, then upload the clip and post your total before the week ends. Rest when you need to, but the clock keeps running until the five minutes are up.</p>
  <a class="btn btn-green weekly-cta" href="#">submit your score now!</a>
  <div class="scores">
    <h3>Latest Scores</h3>
    <table>
      <thead><tr><th>Name</th><th>Athlete Ranking</th><th>Gym Ranking</th><th>Score</th></tr></thead>
      <tbody>
        <tr><td>Marco Lind</td><td>8</td><td>8</td><td>45</td></tr>
        <tr><td>Nadia Hollis</td><td>4</td><td>5</td><td>54</td></tr>
        <tr><td>Jonah Pryce</td><td>6</td><td>7</td><td>65</td></tr>
        <tr><td>Ilsa Varga</td><td>7</td><td>6</td><td>24</td></tr>
        <tr><td>Felix Dunmore</td><td>5</td><td>9</td><td>53</td></tr>
      </tbody>
    </table>
  </div>
</section>

<h2 class="section-title" style="left:118px;top:388px">Current Active Contests</h2>
<h2 class="section-title" style="left:503px;top:388px">Partners</h2>

<article class="contest" style="top:414px">
  <h3 class="contest-title">Run a half marathon in 8 weeks<small>(05:30)</small></h3>
  <div class="status"><span class="tag">Open</span>3 days left</div>
  <p class="contest-desc">Follow the posted plan, log each session and film your final effort from start to finish. Keep good form, pace yourself and stay safe on every rep. Upload your clip with the result and your gym name before the deadline closes. Top entries win prizes, a place on the leaderboard and a feature on the page. Check back daily for updates.</p>
  <a class="btn btn-green contest-submit" href="#">Submit your Score</a>
  <div class="video-thumb" role="img" aria-label="Workout example video still"><svg width="63" height="47" viewBox="0 0 63 47"><circle cx="31.5" cy="23.5" r="8" fill="#8a8a8a" stroke="#bdbdbd"/><path d="M29 19.5l6 4-6 4z" fill="#333"/></svg></div>
  <div class="divider" style="top:87px"></div>
  <h4 class="leaders-title">Top 10 leaders</h4>
  <div class="photo photo-lead" role="img" aria-label="Portrait photo of the gold prize athlete"></div>
  <p class="lead-name">Dario Velt</p>
  <p class="lead-gym">Ironleaf Fitness Club</p>
  <p class="lead-video"><svg class="play-icon" viewBox="0 0 10 10"><circle cx="5" cy="5" r="4.5" fill="none" stroke="#999"/><path d="M4 3l3 2-3 2z" fill="#777"/></svg>Watch Video<small>(05:30)</small></p>
  <p class="lead-prize">Gold Prize</p>
  <div class="runner" style="top:113px"><div class="photo photo-runner" role="img" aria-label="Portrait photo of a silver prize athlete"></div><p class="runner-name">Owen Marsh</p><p class="runner-gym">Ironleaf Fitness Club</p><p class="runner-prize">Silver Prize</p><p class="runner-video"><svg class="play-icon" viewBox="0 0 10 10"><circle cx="5" cy="5" r="4.5" fill="none" stroke="#999"/><path d="M4 3l3 2-3 2z" fill="#777"/></svg>Watch Video</p><p class="runner-time">(05:30)</p></div>
  <div class="runner" style="top:146px"><div class="photo photo-runner" role="img" aria-label="Portrait photo of a silver prize athlete"></div><p class="runner-name">Tobin Hale</p><p class="runner-gym">Northgate Fitness Club</p><p class="runner-prize">Silver Prize</p><p class="runner-video"><svg class="play-icon" viewBox="0 0 10 10"><circle cx="5" cy="5" r="4.5" fill="none" stroke="#999"/><path d="M4 3l3 2-3 2z" fill="#777"/></svg>Watch Video</p><p class="runner-time">(04:28)</p></div>
  <div class="divider" style="top:176px"></div>
  <p class="others-label">Other Contestants</p>
  <div class="others" role="img" aria-label="Portrait photos of other contestants"><div class="photo"></div><div class="photo"></div><div class="photo"></div><div class="photo"></div><div class="photo"></div><div class="photo"></div><div class="photo"></div></div>
</article>

<article class="contest" style="top:648px">
  <h3 class="contest-title">Complete as many push ups as possible in 5 minutes.<small>(05:00)</small></h3>
  <div class="status"><span class="tag">Open</span>5 days left</div>
  <p class="contest-desc">Follow the posted plan, log each session and film your final effort from start to finish. Keep good form, pace yourself and stay safe on every rep. Upload your clip with the result and your gym name before the deadline closes. Top entries win prizes, a place on the leaderboard and a feature on the page. Check back daily for updates.</p>
  <a class="btn btn-green contest-submit" href="#">Submit your Score</a>
  <div class="video-thumb" role="img" aria-label="Workout example video still"><svg width="63" height="47" viewBox="0 0 63 47"><circle cx="31.5" cy="23.5" r="8" fill="#8a8a8a" stroke="#bdbdbd"/><path d="M29 19.5l6 4-6 4z" fill="#333"/></svg></div>
  <div class="divider" style="top:87px"></div>
  <h4 class="leaders-title">Top 10 leaders</h4>
  <div class="photo photo-lead" role="img" aria-label="Portrait photo of the gold prize athlete"></div>
  <p class="lead-name">Dario Velt</p>
  <p class="lead-gym">Ironleaf Fitness Club</p>
  <p class="lead-video"><svg class="play-icon" viewBox="0 0 10 10"><circle cx="5" cy="5" r="4.5" fill="none" stroke="#999"/><path d="M4 3l3 2-3 2z" fill="#777"/></svg>Watch Video<small>(05:30)</small></p>
  <p class="lead-prize">Gold Prize</p>
  <div class="runner" style="top:113px"><div class="photo photo-runner" role="img" aria-label="Portrait photo of a silver prize athlete"></div><p class="runner-name">Owen Marsh</p><p class="runner-gym">Ironleaf Fitness Club</p><p class="runner-prize">Silver Prize</p><p class="runner-video"><svg class="play-icon" viewBox="0 0 10 10"><circle cx="5" cy="5" r="4.5" fill="none" stroke="#999"/><path d="M4 3l3 2-3 2z" fill="#777"/></svg>Watch Video</p><p class="runner-time">(05:30)</p></div>
  <div class="runner" style="top:146px"><div class="photo photo-runner" role="img" aria-label="Portrait photo of a silver prize athlete"></div><p class="runner-name">Tobin Hale</p><p class="runner-gym">Northgate Fitness Club</p><p class="runner-prize">Silver Prize</p><p class="runner-video"><svg class="play-icon" viewBox="0 0 10 10"><circle cx="5" cy="5" r="4.5" fill="none" stroke="#999"/><path d="M4 3l3 2-3 2z" fill="#777"/></svg>Watch Video</p><p class="runner-time">(04:28)</p></div>
  <div class="divider" style="top:176px"></div>
  <p class="others-label">Other Contestants</p>
  <div class="others" role="img" aria-label="Portrait photos of other contestants"><div class="photo"></div><div class="photo"></div><div class="photo"></div><div class="photo"></div><div class="photo"></div><div class="photo"></div><div class="photo"></div></div>
</article>

<article class="contest" style="top:882px">
  <h3 class="contest-title">Praesent vitae felis consectetur, vestibulum ligula et.<small>(04:00)</small></h3>
  <div class="status"><span class="tag">Open</span>2 days left</div>
  <p class="contest-desc">Follow the posted plan, log each session and film your final effort from start to finish. Keep good form, pace yourself and stay safe on every rep. Upload your clip with the result and your gym name before the deadline closes. Top entries win prizes, a place on the leaderboard and a feature on the page. Check back daily for updates.</p>
  <a class="btn btn-green contest-submit" href="#">Submit your Score</a>
  <div class="video-thumb" role="img" aria-label="Workout example video still"><svg width="63" height="47" viewBox="0 0 63 47"><circle cx="31.5" cy="23.5" r="8" fill="#8a8a8a" stroke="#bdbdbd"/><path d="M29 19.5l6 4-6 4z" fill="#333"/></svg></div>
  <div class="divider" style="top:87px"></div>
  <h4 class="leaders-title">Top 10 leaders</h4>
  <div class="photo photo-lead" role="img" aria-label="Portrait photo of the gold prize athlete"></div>
  <p class="lead-name">Dario Velt</p>
  <p class="lead-gym">Ironleaf Fitness Club</p>
  <p class="lead-video"><svg class="play-icon" viewBox="0 0 10 10"><circle cx="5" cy="5" r="4.5" fill="none" stroke="#999"/><path d="M4 3l3 2-3 2z" fill="#777"/></svg>Watch Video<small>(05:30)</small></p>
  <p class="lead-prize">Gold Prize</p>
  <div class="runner" style="top:113px"><div class="photo photo-runner" role="img" aria-label="Portrait photo of a silver prize athlete"></div><p class="runner-name">Owen Marsh</p><p class="runner-gym">Ironleaf Fitness Club</p><p class="runner-prize">Silver Prize</p><p class="runner-video"><svg class="play-icon" viewBox="0 0 10 10"><circle cx="5" cy="5" r="4.5" fill="none" stroke="#999"/><path d="M4 3l3 2-3 2z" fill="#777"/></svg>Watch Video</p><p class="runner-time">(05:30)</p></div>
  <div class="runner" style="top:146px"><div class="photo photo-runner" role="img" aria-label="Portrait photo of a bronze prize athlete"></div><p class="runner-name">Tobin Hale</p><p class="runner-gym">Northgate Fitness Club</p><p class="runner-prize">Bronze Prize</p><p class="runner-video"><svg class="play-icon" viewBox="0 0 10 10"><circle cx="5" cy="5" r="4.5" fill="none" stroke="#999"/><path d="M4 3l3 2-3 2z" fill="#777"/></svg>Watch Video</p><p class="runner-time">(04:28)</p></div>
  <div class="divider" style="top:176px"></div>
  <p class="others-label">Other Contestants</p>
  <div class="others" role="img" aria-label="Portrait photos of other contestants"><div class="photo"></div><div class="photo"></div><div class="photo"></div><div class="photo"></div><div class="photo"></div><div class="photo"></div><div class="photo"></div></div>
</article>

<aside class="partners" aria-label="Advertising partners">
  <div class="partner partner-1"></div>
  <div class="partner partner-2"></div>
  <div class="partner partner-3"></div>
  <div class="partner partner-4"></div>
  <div class="partner partner-5"></div>
  <div class="partner partner-6"></div>
</aside>

<nav class="pager" aria-label="Older contests">
  <svg width="11" height="9" viewBox="0 0 11 9"><path d="M5 1L1.5 4.5 5 8M10 1L6.5 4.5 10 8" fill="none" stroke="var(--blue)"/></svg>
  <svg width="6" height="9" viewBox="0 0 6 9"><path d="M5 1L1.5 4.5 5 8" fill="none" stroke="var(--blue)"/></svg>
  <span class="current">1</span><span>2</span><span>3</span><span>4</span><span>5</span>
  <svg width="6" height="9" viewBox="0 0 6 9"><path d="M1 1l3.5 3.5L1 8" fill="none" stroke="var(--blue)"/></svg>
  <svg width="11" height="9" viewBox="0 0 11 9"><path d="M1 1l3.5 3.5L1 8M6 1l3.5 3.5L6 8" fill="none" stroke="var(--blue)"/></svg>
</nav>

<footer class="site-footer">
  <p class="footer-brand">PeakTrial</p>
  <p class="copyright">Copyright © 2013 PeakTrial.com All rights reserved.</p>
</footer>

</body>
</html>
```